WTR PDAK Thank You card

We need a thank you card to give to our various stakeholders. The card design needs to be professional, corporate, and use elements of our current visual identity (colours and logo will be supplied). The inside of the card needs to have a space for a personal message to be written. Our target card size is 5 x 7.

As a bit of background, we fund local health care in Norvale. We do not directly provide front-line health care services. We do manage the funding and performance monitoring for the agencies we fund. We engage a wide range of people from CEO's, to MPP's, to the general public on a variety of health care topics. At the heart of it, we are a local organization that works to improve health care in Windsor/Essex, Chatham-Kent, and Sarnia/Lambton.

The final design should lean towards a more traditional look.

• It must incorporate our colour pallet and logo

```html
<!DOCTYPE html>
<html lang="en">
<head>
<meta charset="utf-8">
<title>WTR PDAK Thank You Card</title>
<link rel="stylesheet" href="https://fonts.googleapis.com/css2?family=Didact+Gothic&family=Open+Sans:wght@400;600&display=swap">
<style>
  :root {
    --stage: #0e0e0e;
    --card: #6c6c6c;
    --card-light: #747474;
    --band: #3c3c3c;
    --frame: #f2f2f2;
    --ink: #0a0a0a;
    --soft-white: #e4e4e4;
    --mark-dark: #1c1c1c;
    --faint: #8a8a8a;
  }
  * { margin: 0; padding: 0; box-sizing: border-box; }
  html, body {
    width: 1200px;
    height: 900px;
    overflow: hidden;
    background: var(--stage);
  }
  .card {
    position: absolute;
    left: 280px;
    top: 0;
    width: 642px;
    height: 900px;
    background: radial-gradient(ellipse at 40% 30%, var(--card-light), var(--card) 70%);
    overflow: hidden;
  }
  .card-shapes {
    position: absolute;
    inset: 0;
  }
  .corner-name {
    position: absolute;
    left: 46px;
    top: 140px;
    font-family: "Didact Gothic", "Century Gothic", sans-serif;
    font-size: 30px;
    letter-spacing: 4px;
    color: var(--mark-dark);
  }
  .message-prompt {
    position: absolute;
    left: 178px;
    width: 418px;
    top: 501px;
    text-align: center;
    font-family: "Didact Gothic", "Century Gothic", sans-serif;
    font-size: 20px;
    letter-spacing: 1.8px;
    color: var(--frame);
  }
  .thank-you {
    position: absolute;
    left: 48px;
    top: 786px;
    font-family: "Didact Gothic", "Century Gothic", sans-serif;
    font-size: 25px;
    letter-spacing: 18px;
    color: var(--soft-white);
  }
  .signoff-dot {
    position: absolute;
    left: 416px;
    top: 762px;
    width: 38px;
    height: 38px;
    border-radius: 50%;
    background: var(--soft-white);
  }
  .signoff {
    position: absolute;
    left: 478px;
    top: 776px;
    width: 158px;
    font-family: "Open Sans", Arial, sans-serif;
    color: var(--ink);
  }
  .signoff-name {
    font-size: 34px;
    font-weight: 400;
    line-height: 1;
    padding-bottom: 4px;
    border-bottom: 2px solid var(--ink);
  }
  .signoff-line {
    font-size: 11px;
    font-weight: 600;
    line-height: 13.5px;
  }
  .signoff-line.en {
    padding-top: 6px;
    padding-bottom: 3px;
    border-bottom: 1px solid var(--ink);
  }
  .signoff-line.fr { padding-top: 3px; }
</style>
</head>
<body>
  <main class="card" aria-label="WTR PDAK thank you card">
    <svg class="card-shapes" width="642" height="900" viewBox="0 0 642 900" aria-hidden="true">
      <circle class="faint-backdrop" cx="190" cy="470" r="230" fill="var(--faint)" opacity="0.35"/>
      <path class="band" d="M0 772 C 200 752, 420 728, 642 722 L 642 818 L 0 818 Z" fill="var(--band)"/>
      <path class="message-frame" d="M178 748 L178 254 L596 254 L596 720"
            fill="none" stroke="var(--frame)" stroke-width="3"
            stroke-dasharray="0 7" stroke-linecap="round"/>
    </svg>

    <div class="corner-name">WTR PDAK</div>

    <p class="message-prompt">your message</p>

    <p class="thank-you">thank you</p>

    <span class="signoff-dot" aria-hidden="true"></span>
    <div class="signoff">
      <div class="signoff-name">Norvale</div>
      <p class="signoff-line en">WTR PDAK Regional Care<br>Network</p>
      <p class="signoff-line fr">Réseau régional de soins<br>de santé WTR PDAK<br>du secteur sud</p>
    </div>
  </main>
</body>
</html>
```